Fundraiser Brochure for Candle Company

We are a mid-sized candle company. We have been doing fundraisers for many years and need a new design/look for our brochure. Please don't design it to mimic our website - I want that updated as well. I'm looking for more of a Marisa Thornbury, Juniper Hollow look. I want this to be 5.5 w X 8.5 h size but that isn't an option here. I called Quick Press Prints and they said to just put it in the notes - OK there ya go!! We do not need an order form with this as we are going to make a separate sheet to insert for the order form. I'd like the products types (Hayloft Candles, barn brick sets, reflective light candles, soup) each to have their own page. Rooms Sprays and Diffusers can go on the same page since there are only a few of each to select from. The fragrance descriptions can be all on 1 page since there are repeats in the different product types. The soup is a big seller for us :) Please feel free to do what you'd like to with the pix. I know the quality isn't amazing but it's all I have right now. Thank you!!! Dorinda

Font styles to use
Serif

Requirements
Nice to have
• I listed what I'd like in the project descriptions

```html
<!DOCTYPE html>
<html lang="en">
<head>
<meta charset="utf-8">
<title>Hayloft Candle Company – Fundraiser Brochure Spread</title>
<link href="https://fonts.googleapis.com/css2?family=Ubuntu:wght@400;500&family=Dancing+Script:wght@500&display=swap" rel="stylesheet">
<style>
  :root{
    --backdrop:#8e909f;
    --page-cream:#efe7dc;
    --page-edge:#e4e1dd;
    --panel-tan:rgba(226,211,188,.9);
    --field-light:#d8d2c8;
    --field-dark:#a79c8e;
    --ink-maroon:#8a4a3e;
    --tab-rose:#9b6a61;
    --caption-band:#8e5f5b;
    --caption-ink:#f3e9e4;
    --photo-wood:#7d6a5a;
    --photo-dark:#4c4038;
  }
  *{box-sizing:border-box;margin:0;padding:0}
  html,body{width:1200px;height:1000px;overflow:hidden}
  body{background:var(--backdrop);font-family:"Ubuntu",sans-serif;position:relative}

  .spread{position:absolute;left:40px;top:190px;width:1120px;height:620px;display:flex;box-shadow:0 14px 30px rgba(0,0,0,.3)}
  .page{position:relative;width:560px;height:620px;overflow:hidden}

  /* left page */
  .page--intro{background:linear-gradient(180deg,var(--field-light) 0%,#cbc3b7 55%,var(--field-dark) 100%)}
  .page--intro .edge-strip{position:absolute;left:0;top:0;width:56px;height:100%;background:var(--page-edge)}
  .field-photo{position:absolute;left:56px;top:0;right:0;bottom:0;background:linear-gradient(180deg,#dcd6cc 0%,#c9c0b3 50%,#b2a797 100%)}
  .intro-panel{position:absolute;left:100px;top:40px;width:300px;height:560px;background:var(--panel-tan);padding:22px 22px;color:var(--ink-maroon)}
  .brand-name{display:flex;align-items:center;justify-content:center;gap:8px;margin-bottom:24px;font-size:17px;font-weight:500;color:var(--ink-maroon)}
  .brand-name .mark{width:12px;height:12px;background:var(--ink-maroon)}
  .intro-panel p{font-size:13px;line-height:1.45;text-align:justify;margin-bottom:22px}
  .product-column{position:absolute;left:420px;top:20px;width:124px;height:470px;background:var(--page-cream);padding:6px;display:flex;flex-direction:column;gap:6px}
  .product-column .photo{flex:1}
  .photo--jars{background:linear-gradient(160deg,var(--photo-wood),#b2484a 60%,var(--photo-dark))}
  .photo--bricks{background:linear-gradient(160deg,#7a6552,#e0b45a 55%,#c9953f)}
  .photo--sprays{background:linear-gradient(160deg,#8a7868,#3d3733 60%,#6b6058)}

  /* right page */
  .page--catalog{background:radial-gradient(ellipse at 70% 30%,#f4ede3 0%,var(--page-cream) 45%,#e3d7c7 100%)}
  .category-tab{position:absolute;left:22px;top:36px;width:84px;height:84px;background:var(--tab-rose);color:var(--caption-ink);font-family:"Dancing Script",cursive;font-size:30px;display:flex;align-items:center;justify-content:center}
  .catalog-brand{position:absolute;right:28px;top:30px;display:flex;align-items:center;gap:6px;font-size:13px;font-weight:500;color:var(--ink-maroon)}
  .catalog-brand .mark{width:10px;height:10px;background:var(--ink-maroon)}
  .product-grid{position:absolute;left:30px;top:130px;width:510px;display:grid;grid-template-columns:repeat(4,1fr);gap:20px 8px}
  .product-card{background:var(--caption-band);display:flex;flex-direction:column}
  .product-card .photo{height:118px}
  .product-card .caption{height:40px;padding:6px 6px;font-size:9.5px;line-height:1.4;color:var(--caption-ink);text-align:center;white-space:nowrap}
  .jar-white{background:linear-gradient(160deg,var(--photo-wood),#ece4d6 55%,var(--photo-dark))}
  .jar-purple{background:linear-gradient(160deg,var(--photo-wood),#6c4a74 55%,var(--photo-dark))}
  .jar-cream{background:linear-gradient(160deg,var(--photo-wood),#efe1c2 55%,var(--photo-dark))}
  .jar-red{background:linear-gradient(160deg,var(--photo-wood),#9a2f3a 55%,var(--photo-dark))}
  .jar-ivory{background:linear-gradient(160deg,var(--photo-wood),#f1ead9 55%,var(--photo-dark))}
  .jar-yellow{background:linear-gradient(160deg,var(--photo-wood),#e7c12a 55%,var(--photo-dark))}
  .jar-blue{background:linear-gradient(160deg,#4d6a8a,#2f3e55 55%,#6f7f63)}
  .gutter{position:absolute;left:558px;top:0;width:6px;height:620px;background:linear-gradient(90deg,rgba(0,0,0,.12),rgba(0,0,0,0))}
</style>
</head>
<body>
<div class="spread">
  <section class="page page--intro">
    <div class="edge-strip"></div>
    <div class="field-photo" role="img" aria-label="Soft sepia photo of a grassy meadow"></div>
    <div class="intro-panel">
      <div class="brand-name"><span class="mark"></span>Hayloft Candle Company</div>
      <p>The Hayloft Candle Company prides itself on providing you with long lasting, highly fragrant, hand poured candles that will engage your senses and enrich your home.</p>
      <p>Hayloft Candles are offered in 76 captivating fragrances. The essence of a delicate spring garden, the alluring blend of an ocean breeze, the simplicity and spice of the holidays, and even the wholesome aroma of freshly baked cakes and cookies are sensory experiences that charm us and reawaken pleasant memories.</p>
      <p>The process of producing these candles and home fragrance products is meticulous and carefully monitored to ensure high quality products for you to trust and love.</p>
    </div>
    <div class="product-column">
      <div class="photo photo--jars" role="img" aria-label="Photo of red jar candles on a wooden table"></div>
      <div class="photo photo--bricks" role="img" aria-label="Photo of wax brick sets in packaging"></div>
      <div class="photo photo--sprays" role="img" aria-label="Photo of room spray bottles and diffusers"></div>
    </div>
  </section>

  <section class="page page--catalog">
    <div class="category-tab">fruity</div>
    <div class="catalog-brand"><span class="mark"></span>Hayloft</div>
    <div class="product-grid">
      <div class="product-card"><div class="photo jar-white" role="img" aria-label="Photo of pale jar candles"></div><div class="caption">Orchard Peach Soy Jar<br>Candle 14 or 6 oz</div></div>
      <div class="product-card"><div class="photo jar-purple" role="img" aria-label="Photo of purple jar candles"></div><div class="caption">Wild Plum Soy Jar<br>Candle 14 or 6 oz</div></div>
      <div class="product-card"><div class="photo jar-cream" role="img" aria-label="Photo of cream jar candles"></div><div class="caption">Lemon Grove Soy Jar<br>Candle 14 or 6 oz</div></div>
      <div class="product-card"><div class="photo jar-red" role="img" aria-label="Photo of deep red jar candles"></div><div class="caption">Cider Mill Soy Jar<br>Candle 14 or 6 oz</div></div>
      <div class="product-card"><div class="photo jar-red" role="img" aria-label="Photo of red jar candles"></div><div class="caption">Spiced Pear Soy Jar<br>Candle 14 or 6 oz</div></div>
      <div class="product-card"><div class="photo jar-ivory" role="img" aria-label="Photo of ivory jar candles"></div><div class="caption">Melon Mint Soy Jar<br>Candle 14 or 6 oz</div></div>
      <div class="product-card"><div class="photo jar-yellow" role="img" aria-label="Photo of yellow jar candles"></div><div class="caption">Pineapple Cake Soy Jar<br>Candle 14 or 6 oz</div></div>
      <div class="product-card"><div class="photo jar-blue" role="img" aria-label="Photo of a blue jar candle outdoors"></div><div class="caption">Hayloft Harvest Soy Jar<br>Candle 14 oz</div></div>
    </div>
  </section>
  <div class="gutter"></div>
</div>
</body>
</html>
```